BRT Flyer 2022

Need a flyer/Brochure it it an information piece on or company to give to clients during Sales call. I have started something in Canva but would like it more professional designed. We we are a Fire & Security company.
we do alot of cloud based systems. New system intercoms, Camera systems, Card Access and fire alarm systems

```html
<!DOCTYPE html>
<html lang="en">
<head>
<meta charset="utf-8">
<title>BRT Fire &amp; Security Brochure</title>
<link href="https://fonts.googleapis.com/css2?family=Montserrat:wght@400;600;700;800;900&family=Open+Sans:wght@400;600&display=swap" rel="stylesheet">
<style>
  :root{
    --red:#e3202a;
    --red-dark:#b5141c;
    --ink:#1b1b1e;
    --ink-soft:#2a2a2e;
    --paper:#ffffff;
    --muted:#9a9aa0;
    --text:#555559;
    --stage:#dcdcdc;
  }
  *{box-sizing:border-box;margin:0;padding:0}
  html,body{width:876px;height:1200px;overflow:hidden;background:var(--stage)}
  body{position:relative;font-family:"Open Sans",Arial,sans-serif}
  .sheet{position:absolute;left:28px;width:820px;height:540px;display:flex;box-shadow:0 6px 18px rgba(0,0,0,.25)}
  .sheet--outer{top:40px}
  .sheet--inner{top:620px}
  .panel{position:relative;width:273.33px;height:100%;overflow:hidden}
  .panel--dark{background:var(--ink);color:#fff}
  .panel--light{background:var(--paper);color:var(--ink)}
  .deco{position:absolute;inset:0;width:100%;height:100%}
  .photo{position:absolute}
  h2,h3,.brand,.tagline{font-family:"Montserrat",Arial,sans-serif}
  .body-copy{font-size:8.5px;line-height:1.55}

  /* outer: testimonial */
  .testimonial{position:absolute;left:24px;top:26px;width:225px;z-index:2}
  .testimonial h2{font-size:22px;font-weight:800;margin-bottom:12px}
  .testimonial .body-copy{color:#c9c9cd}
  .testimonial .author{margin-top:8px;font-size:8px;color:var(--muted)}
  .photo--intercom{left:24px;top:270px;width:225px;height:150px;background:linear-gradient(135deg,#3b4e66,#8fa9c2 55%,#2b3440);border:5px solid #111}

  /* outer: contact */
  .brand{font-weight:900;color:var(--red);letter-spacing:1px;display:flex;align-items:center;gap:6px}
  .brand-mark{width:10px;height:10px;background:var(--red)}
  .brand-block{position:absolute;left:0;right:0;top:120px;text-align:center;z-index:2}
  .brand-block .brand{font-size:40px;justify-content:center}
  .brand-sub{font-size:7px;font-weight:700;letter-spacing:1.5px;text-transform:uppercase;color:var(--ink)}
  .contact{position:absolute;left:0;right:0;top:190px;text-align:center;z-index:2}
  .contact .eyebrow{font-size:9px;color:var(--red);font-weight:600}
  .contact h2{font-size:26px;font-weight:800;margin-bottom:16px}
  .contact-list{list-style:none;display:flex;flex-direction:column;align-items:center;gap:12px}
  .contact-list li{display:flex;flex-direction:column;align-items:center;gap:4px;font-size:8px;color:var(--text)}
  .contact-list svg{width:12px;height:12px}
  .brand--corner{position:absolute;right:20px;bottom:34px;font-size:22px;z-index:2}

  /* outer: cover */
  .photo--touch{left:0;top:0;width:100%;height:320px;background:linear-gradient(150deg,#5a5f69,#c8ccd3 45%,#3c3f46);clip-path:polygon(0 0,100% 0,100% 70%,0 100%)}
  .cover-title{position:absolute;left:22px;top:400px;z-index:2}
  .tagline{font-size:27px;font-weight:900;line-height:1;color:#fff}
  .tagline span{display:block;font-size:18px;color:var(--red);margin-top:4px}
  .web{position:absolute;left:22px;bottom:22px;font-size:9px;font-weight:600;color:#fff}

  /* inner: why choose */
  .photo--detector{left:0;top:0;width:100%;height:270px;background:linear-gradient(160deg,#f2f2f2,#b31b22 55%,#4a1013);clip-path:polygon(0 0,100% 0,100% 75%,0 100%)}
  .why{position:absolute;left:22px;top:300px;width:230px;z-index:2}
  .why h2{font-size:34px;font-weight:900;line-height:1;margin-bottom:12px}
  .why .body-copy{color:var(--text)}
  .why .author{margin-top:26px;font-size:11px;color:var(--text)}

  /* inner: services */
  .services{position:absolute;left:0;right:0;top:22px;padding:0 26px;z-index:2}
  .services h3{font-size:15px;font-weight:700;text-align:center;margin-bottom:22px}
  .service{display:flex;flex-direction:column;align-items:center;text-align:center;margin-bottom:22px}
  .service-icon{width:34px;height:34px;border-radius:50%;background:var(--red);display:flex;align-items:center;justify-content:center;margin-bottom:6px}
  .service-icon svg{width:18px;height:18px}
  .service h4{font-family:"Montserrat",Arial,sans-serif;font-size:11px;font-weight:700;margin-bottom:3px}
  .service p{font-size:8px;color:#bfbfc4}

  /* inner: about */
  .about{position:absolute;left:22px;top:24px;width:230px;z-index:2}
  .about h2{font-size:30px;font-weight:900;margin-bottom:10px}
  .about .body-copy{color:var(--text)}
  .photo--station{left:0;top:220px;width:100%;height:320px;background:linear-gradient(140deg,#2c2c30,#8d8f94 50%,#1e1e21);clip-path:polygon(0 22%,100% 0,100% 100%,0 100%)}
</style>
</head>
<body>

<section class="sheet sheet--outer">
  <article class="panel panel--dark">
    <svg class="deco" viewBox="0 0 273 540" preserveAspectRatio="none" aria-hidden="true">
      <polygon points="180,0 273,0 273,60" fill="var(--red)"/>
      <polygon points="0,470 120,540 0,540" fill="var(--red)"/>
      <polygon points="273,440 273,540 150,540" fill="var(--ink-soft)"/>
    </svg>
    <div class="testimonial">
      <h2>Client Testimonial</h2>
      <p class="body-copy">Working with BRT transformed how we protect our building. Their team designed a cloud based access and camera system that is simple to manage, and their response time on service calls has been outstanding every single time.</p>
      <p class="author">— Facilities Manager, Harbor Point Offices</p>
    </div>
    <div class="photo photo--intercom" role="img" aria-label="Photo of a wall-mounted video intercom touchscreen"></div>
  </article>

  <article class="panel panel--light">
    <svg class="deco" viewBox="0 0 273 540" preserveAspectRatio="none" aria-hidden="true">
      <polygon points="0,0 110,0 0,95" fill="var(--ink)"/>
      <polygon points="110,0 150,0 0,130 0,95" fill="var(--red)"/>
      <polygon points="273,410 273,540 110,540" fill="var(--ink)"/>
      <polygon points="273,380 273,410 110,540 75,540" fill="var(--red)"/>
    </svg>
    <div class="brand-block">
      <div class="brand">BRT</div>
      <div class="brand-sub">Fire &amp; Security Systems</div>
    </div>
    <div class="contact">
      <p class="eyebrow">Get in Touch</p>
      <h2>Contact</h2>
      <ul class="contact-list">
        <li><svg viewBox="0 0 24 24"><path d="M6 2h4l2 5-3 2a12 12 0 0 0 6 6l2-3 5 2v4a2 2 0 0 1-2 2A18 18 0 0 1 4 4a2 2 0 0 1 2-2z" fill="var(--red)"/></svg>(555) 014-2290</li>
        <li><svg viewBox="0 0 24 24"><rect x="2" y="5" width="20" height="14" rx="2" fill="var(--red)"/><path d="M3 6l9 7 9-7" stroke="#fff" stroke-width="2" fill="none"/></svg>info@brtsecurity.com</li>
        <li><svg viewBox="0 0 24 24"><path d="M12 2a7 7 0 0 0-7 7c0 5 7 13 7 13s7-8 7-13a7 7 0 0 0-7-7z" fill="var(--red)"/><circle cx="12" cy="9" r="2.5" fill="#fff"/></svg>120 Harbor Lane, Springfield</li>
      </ul>
    </div>
    <div class="brand brand--corner">BRT</div>
  </article>

  <article class="panel panel--dark">
    <div class="photo photo--touch" role="img" aria-label="Photo of a hand touching a glowing digital security interface"></div>
    <svg class="deco" viewBox="0 0 273 540" preserveAspectRatio="none" aria-hidden="true">
      <polygon points="0,320 273,224 273,250 0,346" fill="var(--red)"/>
      <polygon points="180,0 273,0 273,40 230,0" fill="var(--red)"/>
      <polygon points="0,0 60,0 0,70" fill="var(--red)"/>
    </svg>
    <div class="cover-title">
      <p class="tagline">UNLOCKING<span>THE FURTURE</span></p>
    </div>
    <p class="web">www.brtsecurity.com</p>
  </article>
</section>

<section class="sheet sheet--inner">
  <article class="panel panel--light">
    <div class="photo photo--detector" role="img" aria-label="Photo of a ceiling smoke detector and a red fire alarm panel"></div>
    <svg class="deco" viewBox="0 0 273 540" preserveAspectRatio="none" aria-hidden="true">
      <polygon points="0,270 273,202 273,226 0,294" fill="var(--red)"/>
      <polygon points="160,0 273,0 273,70" fill="var(--ink)"/>
    </svg>
    <div class="why">
      <h2>Why<br>Choose Us</h2>
      <p class="body-copy">We design, install and service complete fire and security systems, backed by licensed technicians, local support and cloud tools that keep every site protected around the clock.</p>
      <p class="author">- Anonymous</p>
    </div>
  </article>

  <article class="panel panel--dark">
    <svg class="deco" viewBox="0 0 273 540" preserveAspectRatio="none" aria-hidden="true">
      <polygon points="0,0 40,0 0,40" fill="var(--red)"/>
      <polygon points="273,500 273,540 233,540" fill="var(--red)"/>
    </svg>
    <div class="services">
      <h3>Company Services</h3>
      <div class="service">
        <span class="service-icon"><svg viewBox="0 0 24 24"><path d="M7 18a5 5 0 0 1-.5-10A6 6 0 0 1 18 9a4.5 4.5 0 0 1-.5 9z" fill="#fff"/></svg></span>
        <h4>Cloud Services</h4>
        <p>Manage doors and cameras from anywhere.</p>
      </div>
      <div class="service">
        <span class="service-icon"><svg viewBox="0 0 24 24"><rect x="6" y="2" width="12" height="20" rx="2" fill="#fff"/><rect x="8" y="5" width="8" height="6" fill="var(--red)"/><circle cx="12" cy="16" r="2" fill="var(--red)"/></svg></span>
        <h4>Intercom &amp; Access</h4>
        <p>Video intercoms and card access control.</p>
      </div>
      <div class="service">
        <span class="service-icon"><svg viewBox="0 0 24 24"><path d="M12 2c1 4 6 6 6 12a6 6 0 0 1-12 0c0-3 2-5 3-6 0 2 1 3 2 3 0-3-1-6 1-9z" fill="#fff"/></svg></span>
        <h4>Fire Alarm</h4>
        <p>Detection, monitoring and code compliant panels.</p>
      </div>
      <div class="service">
        <span class="service-icon"><svg viewBox="0 0 24 24"><rect x="3" y="7" width="13" height="8" rx="1" fill="#fff"/><path d="M16 9l5-2v8l-5-2z" fill="#fff"/><rect x="7" y="15" width="2" height="5" fill="#fff"/></svg></span>
        <h4>Camera Systems</h4>
        <p>HD cameras with remote cloud viewing.</p>
      </div>
    </div>
  </article>

  <article class="panel panel--light">
    <div class="about">
      <h2>About us</h2>
      <p class="body-copy">BRT Fire &amp; Security Systems protects offices, schools and properties with modern, connected safety solutions. From first survey to ongoing service, our team delivers reliable systems built around each client's needs and budget.</p>
    </div>
    <div class="photo photo--station" role="img" aria-label="Photo of a fire alarm pull station, a security camera and a keypad"></div>
    <svg class="deco" viewBox="0 0 273 540" preserveAspectRatio="none" aria-hidden="true">
      <polygon points="0,290 273,220 273,240 0,310" fill="var(--red)"/>
      <polygon points="273,470 273,540 170,540" fill="var(--red)"/>
      <polyline points="40,540 150,390 273,430" fill="none" stroke="#fff" stroke-width="3"/>
    </svg>
  </article>
</section>

</body>
</html>
```